KVT website

Im a Specialty contractor that specializes in fireproofing. Epoxy flooring and terrazo along with poured floors and polished concrete.

We also do fire caulking.

Im the largest specialty flooring healthcare contractor in the south east.

Dane

Contractor

```html
<!DOCTYPE html>
<html lang="en">
<head>
<meta charset="utf-8">
<title>KVT — Fireproofing Contractor</title>
<link href="https://fonts.googleapis.com/css2?family=Open+Sans:wght@400;600;700;800&display=swap" rel="stylesheet">
<style>
:root{
  --ink:#1d1d1d;
  --text:#555;
  --muted:#8a8a8a;
  --orange:#f26a1b;
  --dark:#2b2b2b;
  --darker:#1c1c1c;
  --line:#dcdcdc;
  --white:#fff;
}
*{box-sizing:border-box;margin:0;padding:0}
html,body{width:1200px;height:2748px;overflow:hidden;background:var(--white)}
body{font-family:"Open Sans",Arial,sans-serif;color:var(--text);font-size:13px;line-height:1.5}
.wrap{width:900px;margin:0 auto;position:relative}
.ph{display:block}

/* top bar */
.topbar{height:24px;background:var(--darker)}
.topbar .wrap{display:flex;justify-content:flex-end;gap:8px;align-items:center;height:24px}
.topbar .sq{width:12px;height:12px;background:#555}
.topbar .mini{color:#bbb;font-size:10px;margin-left:6px}

/* header */
.header{height:224px;position:relative}
.brand{position:absolute;left:0;top:70px}
.brand-row{display:flex;align-items:center;gap:12px}
.brand-mark{width:30px;height:30px;background:var(--ink)}
.brand-name{font-weight:700;font-size:44px;line-height:1;color:var(--ink)}
.brand-sub{font-size:12px;color:var(--muted);margin-top:8px}
.call{position:absolute;right:0;top:110px;font-size:14px;color:var(--text)}
.call b{color:var(--orange)}
.nav{position:absolute;right:0;top:144px;display:flex;background:var(--dark)}
.nav a{color:#ddd;font-size:12px;font-weight:700;padding:9px 20px;text-decoration:none;text-transform:uppercase}
.nav a.home{background:#111;color:var(--white)}
.nav a.active{background:#111}
.dropdown{position:absolute;right:285px;top:180px;width:170px;background:#111;z-index:5}
.dropdown li{list-style:none;color:#ccc;font-size:11px;padding:8px 14px;border-bottom:1px solid #333;text-transform:uppercase}

/* slider */
.slider{height:312px;background:#3a3a3a}
.slider .wrap{height:312px}
.slide-photo{position:absolute;left:0;top:0;width:900px;height:296px;background:linear-gradient(100deg,#6b6d72 0%,#b8bcc2 35%,#8c5a52 55%,#d9dadc 75%,#f1f1f1 100%)}
.slide-text{position:absolute;right:20px;top:110px;width:300px;background:rgba(255,255,255,.92);padding:16px 18px;font-size:13px;color:#444}
.arrow{position:absolute;top:128px;width:40px;height:40px;border-radius:50%;background:rgba(0,0,0,.55)}
.arrow.l{left:-20px}.arrow.r{right:-20px}
.dots{position:absolute;right:24px;top:270px;display:flex;gap:6px}
.dots i{width:8px;height:8px;border-radius:50%;background:#ccc}
.dots i:first-child{background:var(--orange)}

/* tabs */
.tabband{height:132px;background:linear-gradient(#d8d8d8,#f2f2f2)}
.tabs{display:flex;gap:12px;padding-top:32px}
.tab{flex:1;height:68px;background:linear-gradient(#f4f4f4,#cfcfcf);border:1px solid #c4c4c4;display:flex;align-items:center;padding-left:26px;gap:14px;font-size:24px;color:#666}
.tab svg{width:26px;height:26px}

/* section headings */
h2{font-size:24px;font-weight:800;color:var(--ink);padding-bottom:8px;border-bottom:1px solid var(--line);margin-bottom:22px}

/* welcome */
.welcome{padding-top:32px;height:200px}
.welcome .wrap{display:flex;gap:40px}
.welcome-copy{flex:1}
.welcome h1{font-size:27px;font-weight:800;color:var(--ink);line-height:1.2}
.welcome h3{font-size:16px;font-weight:600;color:#333;margin:4px 0 8px}
.welcome p{font-size:12px}
.btn{display:inline-block;background:var(--darker);color:var(--white);font-size:12px;font-weight:600;padding:7px 16px}
.welcome .btn{float:right;margin-top:10px}
.welcome-photo{width:280px;height:128px;background:linear-gradient(120deg,#9fb0bb,#e6ebee 60%,#c3ccd2)}

/* projects */
.projects{padding-top:20px}
.grid{display:grid;grid-template-columns:repeat(4,1fr);gap:30px 28px}
.card .img{height:150px}
.card h4{font-size:15px;font-weight:700;color:var(--ink);margin-top:8px;line-height:1.2}
.card .sub{font-size:11px;color:var(--muted)}
.card p{font-size:11px;margin-top:4px}
.more{text-align:right;margin-top:18px}

/* services */
.services{padding-top:44px}
.services .intro{font-size:12px}
.cols{display:flex;gap:40px;margin-top:18px}
.col{flex:1}
.col h5{font-size:18px;font-weight:600;color:#333;margin-bottom:10px}
.col li{list-style:none;font-size:11px;padding:6px 0;border-bottom:1px dotted var(--line)}

/* team */
.team{padding-top:40px}
.members{display:flex;gap:60px;padding-left:60px}
.member{width:150px}
.member .img{height:150px;border:4px solid #eee;background:linear-gradient(#cfd8de,#eef1f3)}
.member h6{font-size:14px;font-weight:700;color:var(--ink);text-align:center;margin-top:10px}
.member .role{font-size:11px;text-align:center;color:var(--muted)}
.member .link{font-size:11px;text-align:center;color:var(--orange)}

/* footer */
.footer{position:absolute;left:0;top:2328px;width:1200px;height:420px;background:var(--dark);color:#aaa}
.fcols{display:flex;gap:40px;padding-top:36px}
.fcol{flex:1}
.fcol h5{color:var(--white);font-size:16px;font-weight:700;margin-bottom:14px}
.fcol li{list-style:none;font-size:11px;padding:4px 0;border-bottom:1px solid #3c3c3c}
.fcol p{font-size:11px;line-height:1.7}
.recent{display:flex;gap:10px;margin-bottom:12px}
.recent .img{width:64px;height:44px;flex:none}
.recent b{color:var(--white);font-size:12px;display:block}
.recent span{font-size:10px}
.field{height:26px;background:#3d3d3d;border:1px solid #4a4a4a;margin-bottom:8px;font-size:11px;padding:4px 8px;color:#888}
.submit{background:var(--orange);color:var(--white);font-size:11px;font-weight:700;padding:5px 14px;display:inline-block}
.socials{display:flex;gap:8px;margin-top:20px}
.socials i{width:26px;height:26px;background:#555}
.bottom{position:absolute;left:0;bottom:0;width:1200px;height:40px;background:var(--darker);font-size:10px;color:#777}
.bottom .wrap{text-align:right;line-height:40px}
</style>
</head>
<body>

<div class="topbar"><div class="wrap"><span class="sq"></span><span class="sq"></span><span class="sq"></span><span class="sq"></span><span class="mini">1-800-555-0147</span></div></div>

<header class="header">
  <div class="wrap">
    <div class="brand">
      <div class="brand-row"><span class="brand-mark"></span><span class="brand-name">KVT</span></div>
      <div class="brand-sub">Fireproofing contractor · Est. 1998 · Dane</div>
    </div>
    <div class="call">Call us now: <b>1-800-555-0147</b></div>
    <nav class="nav">
      <a class="home">Home</a><a>About</a><a class="active">Projects</a><a>Team</a><a>Blog</a><a>Contact</a>
    </nav>
    <ul class="dropdown"><li>Fireproofing</li><li>Flooring</li><li>Maintenance</li></ul>
  </div>
</header>

<section class="slider">
  <div class="wrap">
    <div class="slide-photo ph" role="img" aria-label="Photo of a polished epoxy floor in a modern healthcare corridor"></div>
    <div class="slide-text">We are Specialty contractor that specializes in fireproofing, Epoxy flooring and terrazo along with poured floors and polished concrete. We also do fire caulking.</div>
    <span class="arrow l"></span><span class="arrow r"></span>
    <div class="dots"><i></i><i></i><i></i><i></i><i></i></div>
  </div>
</section>

<section class="tabband">
  <div class="wrap tabs">
    <div class="tab"><svg viewBox="0 0 26 26"><path d="M13 2c2 6 8 8 8 15a8 8 0 0 1-16 0c0-5 4-8 8-15z" fill="#777"/></svg>Fireproofing</div>
    <div class="tab"><svg viewBox="0 0 26 26"><rect x="2" y="2" width="10" height="10" fill="#777"/><rect x="14" y="2" width="10" height="10" fill="#777"/><rect x="2" y="14" width="10" height="10" fill="#777"/><rect x="14" y="14" width="10" height="10" fill="#777"/></svg>Flooring</div>
    <div class="tab"><svg viewBox="0 0 26 26"><rect x="3" y="3" width="20" height="20" fill="none" stroke="#777" stroke-width="3"/><path d="M8 13h10M13 8v10" stroke="#777" stroke-width="3"/></svg>Maintenance</div>
  </div>
</section>

<section class="welcome">
  <div class="wrap">
    <div class="welcome-copy">
      <h1>Welcome to Our Company</h1>
      <h3>We are Specialty contractor that specializes in fireproofing</h3>
      <p>The largest specialty flooring healthcare contractor in the south east. We install epoxy flooring, terrazo, poured floors and polished concrete, and provide fire caulking for hospitals, clinics and commercial buildings. Every crew is trained, certified and focused on clean, safe, on-schedule work with lasting results.</p>
      <span class="btn">Read more</span>
    </div>
    <div class="welcome-photo ph" role="img" aria-label="Photo of a finished commercial interior with glossy flooring"></div>
  </div>
</section>

<section class="projects">
  <div class="wrap">
    <h2>Our Project</h2>
    <div class="grid">
      <div class="card"><div class="img ph" role="img" aria-label="Photo of sprayed fireproofing on steel beams" style="background:linear-gradient(#4a4a4a,#9a9a9a)"></div><h4>Fireproof project</h4><div class="sub">Medical Center</div><p>Spray applied fireproofing on structural steel for a new hospital wing.</p></div>
      <div class="card"><div class="img ph" role="img" aria-label="Photo of a worker applying fireproofing" style="background:linear-gradient(#d7d7d7,#8d8d8d)"></div><h4>Fireproof project</h4><div class="sub">Office Tower</div><p>Intumescent coating and fire caulking across twelve floors.</p></div>
      <div class="card"><div class="img ph" role="img" aria-label="Photo of subfloor preparation" style="background:linear-gradient(#c79a62,#8c6a44)"></div><h4>Subfloor project</h4><div class="sub">Clinic Renovation</div><p>Leveling and poured underlayment ready for a seamless finish.</p></div>
      <div class="card"><div class="img ph" role="img" aria-label="Photo of crew working on a rooftop deck" style="background:linear-gradient(#9fb3c4,#5e6a72)"></div><h4>Fireproof project</h4><div class="sub">Parking Deck</div><p>Fire rated coating on exposed deck steel and columns.</p></div>
      <div class="card"><div class="img ph" role="img" aria-label="Photo of a glossy red epoxy floor" style="background:linear-gradient(#b8453c,#e7d4cf)"></div><h4>Epoxy Flooring project</h4><div class="sub">Surgery Suite</div><p>Seamless epoxy system with integral cove base for easy cleaning.</p></div>
      <div class="card"><div class="img ph" role="img" aria-label="Photo of a polished epoxy hallway" style="background:linear-gradient(#8a8f95,#e2e4e6)"></div><h4>Epoxy Flooring project</h4><div class="sub">Patient Ward</div><p>Slip resistant finish installed in phases around live operations.</p></div>
      <div class="card"><div class="img ph" role="img" aria-label="Photo of a warehouse with epoxy floor" style="background:linear-gradient(#c9b48f,#7a6a55)"></div><h4>Epoxy Flooring project</h4><div class="sub">Distribution Hub</div><p>Heavy duty coating with safety striping for forklift traffic.</p></div>
      <div class="card"><div class="img ph" role="img" aria-label="Photo of a building under construction" style="background:linear-gradient(#a9c7db,#6b8a6a)"></div><h4>Fireproof project</h4><div class="sub">School Campus</div><p>Full fireproofing package delivered ahead of schedule.</p></div>
    </div>
    <div class="more"><span class="btn">More Project</span></div>
  </div>
</section>

<section class="services">
  <div class="wrap">
    <h2>Our Services</h2>
    <p class="intro">From fireproofing and fire caulking to epoxy, terrazo, poured floors and polished concrete, we handle every step with our own crews. We plan around occupied buildings, protect sensitive areas and deliver durable, code compliant results for healthcare, education and commercial clients across the south east.</p>
    <div class="cols">
      <div class="col"><h5>Fireproofing</h5><ul><li>Spray applied fireproofing</li><li>Intumescent coatings</li><li>Fire caulking and firestop</li><li>Structural steel protection</li><li>Inspection and repair</li><li>Code compliance reports</li></ul></div>
      <div class="col"><h5>Flooring</h5><ul><li>Epoxy flooring systems</li><li>Terrazo installation</li><li>Poured floors</li><li>Polished concrete</li><li>Healthcare flooring</li><li>Surface preparation</li></ul></div>
      <div class="col"><h5>Maintenance</h5><ul><li>Floor cleaning and sealing</li><li>Recoating and repairs</li><li>Concrete polishing upkeep</li><li>Firestop inspections</li><li>Scheduled service plans</li><li>Emergency response</li></ul></div>
    </div>
  </div>
</section>

<section class="team">
  <div class="wrap">
    <h2>Our Team</h2>
    <div class="members">
      <div class="member"><div class="img ph" role="img" aria-label="Portrait of team member Mara Ellis"></div><h6>Mara Ellis</h6><div class="role">Creative Producer</div><div class="link">View profile page »</div></div>
      <div class="member"><div class="img ph" role="img" aria-label="Portrait of team member Owen Pratt"></div><h6>Owen Pratt</h6><div class="role">Project Manager</div><div class="link">View profile page »</div></div>
      <div class="member"><div class="img ph" role="img" aria-label="Portrait of team member Lena Ortiz"></div><h6>Lena Ortiz</h6><div class="role">Accounting</div><div class="link">View profile page »</div></div>
      <div class="member"><div class="img ph" role="img" aria-label="Portrait of team member Ravi Chen"></div><h6>Ravi Chen</h6><div class="role">Site Supervisor</div><div class="link">View profile page »</div></div>
    </div>
  </div>
</section>

<footer class="footer">
  <div class="wrap fcols">
    <div class="fcol"><h5>About Us</h5><p>218 Harbor Lane<br>Southeast District<br>Tel: 1-800-555-0147<br>Email: hello@kvtfloors.example</p></div>
    <div class="fcol"><h5>Blogs</h5><ul><li>Choosing the right epoxy system</li><li>Why fire caulking matters</li><li>Terrazo in healthcare spaces</li><li>Polished concrete care tips</li><li>Fireproofing code updates</li></ul></div>
    <div class="fcol"><h5>Recent Project</h5>
      <div class="recent"><div class="img ph" role="img" aria-label="Thumbnail of a terrazo floor" style="background:#8c8c8c"></div><div><b>Terrazo Floor</b><span>Medical Center</span></div></div>
      <div class="recent"><div class="img ph" role="img" aria-label="Thumbnail of an epoxy floor" style="background:#9a6b5e"></div><div><b>Epoxy Floor</b><span>Patient Ward</span></div></div>
      <div class="recent"><div class="img ph" role="img" aria-label="Thumbnail of fireproofed steel" style="background:#6d7a84"></div><div><b>Fireproofing</b><span>Office Tower</span></div></div>
    </div>
    <div class="fcol"><h5>Newsletter</h5><div class="field">Name</div><div class="field">Email</div><span class="submit">SUBMIT</span><div class="socials"><i></i><i></i><i></i></div></div>
  </div>
  <div class="bottom"><div class="wrap">Copyright © KVT Fireproofing Contractor. All rights reserved.</div></div>
</footer>

</body>
</html>
```